Gourmet food company looking for a dazzling label for their premuim vinagrette dressings

Need a food label that will dazzle our customer and prove what a premium product we have. We make high end gourmet dressing for vegetables, fruit, meat, poultry and fish.

Our label will fit on a 250 mil Tolvenka Square bottle. Labels should be a 4x5 or even 5x5 depending on the design. Nutritionals, bar codes and company blurb will be supplied later. We really want to test you all's talent on this one and are very excited to see your renderings!

Our dressings are Champagne Pear Vinaigrette, White Balsmic Vinaigrette, Mojito Lime Vinaigrette, Creamy-Avacado Lime Vinaigrette, and Asian Sesame Vinaigrette. I hope these names will help you envision our product and kinda what we are looking for.
Updates

Thank you all so far for your renderings.I really don't want pictures if that helps. Our logo can be smaller and/or the name of the product bigger. Perhaps we can even redesign Velora and remove the leaf as I don't really care for what I see yet.So good luck and thanks Added Friday, August 19, 2016

I am still looking for that clean - elegant design for our product as our product is just that. If you look on the internet at vinegars and oils you will see many designs that are simple yet elegant. Creative lettering, bordering, color (can be black and white) and size will help accomplish this. So I invite you to use all your creativity and help me find just what we need.Many thanks Added Tuesday, August 23, 2016

Project Deadline Extended Reason: So many great designs coming in that I wanted a few extra days to tweek!Great job all Added Friday, August 26, 2016

Project Deadline Extended Reason: Very good designs thus far. We just need a few more days.Thanks Added Wednesday, August 31, 2016

Target Market(s)

High end grocery and specialty stores.

Our side panel on the label will say "At Velora we're fanatics for great flavors and are passionate about finding the best ingredients. From simple to elegant our products are "simply velora".

Industry/Entity Type

It Company

Font styles to use
Serif
Decorative
Script

Requirements
Must have
• A label that will draw the consumer to pick it up! Need something bold and elegant...
Nice to have
• Again, I really would like to have a label that pops. Since the bottle front is only about 2inches in width it will need some creativity. Would like something very simple and elegant.
• If the designer does not like the logo, please feel free to design without it!
Should not have
• Dark dark colors. We are selling dressing and we don't want any colors that may distort the contents.
• No stock photos for the front. I don't want our dressing to look like the others on the self. Brambleth Kitchen just uses lettering and a their packaging is eye catching

```html
<!DOCTYPE html>
<html lang="en">
<head>
<meta charset="utf-8">
<title>Velora – Vinaigrette Label</title>
<link rel="stylesheet" href="https://fonts.googleapis.com/css2?family=Marcellus&family=Didact+Gothic&display=swap">
<style>
  :root {
    --gold: #b39a3a;
    --lime: #8aee2c;
    --cream: #eeead7;
    --mint: #eafadc;
    --brown: #35240e;
    --leaf-green: #58b42a;
    --white: #ffffff;
  }
  html, body {
    margin: 0;
    padding: 0;
    width: 1200px;
    height: 1007px;
    overflow: hidden;
    background: var(--white);
  }
  .label {
    position: relative;
    width: 1200px;
    height: 1007px;
  }
  .label__art {
    position: absolute;
    inset: 0;
  }
  .brand {
    position: absolute;
    left: 0;
    width: 1220px;
    top: 470px;
    text-align: center;
    font-family: "Marcellus", serif;
    font-size: 96px;
    line-height: 1;
    color: var(--brown);
    margin: 0;
    font-weight: 400;
  }
  .tagline {
    position: absolute;
    left: 0;
    width: 1220px;
    top: 578px;
    text-align: center;
    font-family: "Didact Gothic", sans-serif;
    font-size: 21px;
    letter-spacing: 1px;
    color: var(--leaf-green);
    margin: 0;
  }
  .flavours {
    position: absolute;
    left: 0;
    width: 1220px;
    top: 742px;
    text-align: center;
    font-family: "Didact Gothic", sans-serif;
    font-size: 23px;
    line-height: 30.5px;
    color: var(--white);
    margin: 0;
  }
</style>
</head>
<body>
<main class="label">
  <svg class="label__art" width="1200" height="1007" viewBox="0 0 1200 1007" aria-hidden="true">
    <defs>
      <clipPath id="outer-disc"><circle cx="610" cy="501" r="500"/></clipPath>
      <clipPath id="inner-disc"><circle cx="610" cy="501" r="472"/></clipPath>
    </defs>
    <!-- rim and field -->
    <circle cx="610" cy="501" r="500" fill="var(--gold)"/>
    <circle cx="610" cy="501" r="477" fill="var(--white)"/>
    <circle cx="610" cy="501" r="472" fill="var(--lime)"/>
    <!-- band across the rim -->
    <g clip-path="url(#outer-disc)">
      <rect x="0" y="321" width="1200" height="344" fill="var(--cream)"/>
      <rect x="0" y="346" width="1200" height="4" fill="var(--gold)"/>
      <rect x="0" y="636" width="1200" height="4" fill="var(--gold)"/>
    </g>
    <!-- band inside the field -->
    <g clip-path="url(#inner-disc)">
      <rect x="0" y="321" width="1200" height="344" fill="var(--mint)"/>
      <rect x="0" y="346" width="1200" height="4" fill="var(--lime)"/>
      <rect x="0" y="636" width="1200" height="4" fill="var(--lime)"/>
    </g>
  </svg>

  <h1 class="brand">Velora</h1>
  <p class="tagline">Wonderfully Indulgent Dressing</p>
  <p class="flavours">
    Our dressings are Champagne Pear Vinaigrette,<br>
    White Balsmic Vinaigrette, Mojito Lime Vinaigrette,<br>
    Creamy-Avacado Lime Vinaigrette,<br>
    and Asian Sesame Vinaigrette.<br>
    .
  </p>
</main>
</body>
</html>
```